Tallowreed Advisory Partners Business Card Design

We have the logo we just need someone to design a modern business card design.

Name: Desmond Munkalt
Phone: 3055550148
Mobile: 9175550193
Web:www.tallowreedadvisory.example
email: dmunkalt@tallowreedadvisory.example
Company: Tallowreed Advisory Partners
Title: CEO

Address: 718 Quillmore Ave, Miami, Florida 33190

Target Market(s)

companies over 100 employees

Industry/Entity Type

Business

```html
<!DOCTYPE html>
<html lang="en">
<head>
<meta charset="utf-8">
<title>Tallowreed Advisory Partners Business Card</title>
<link rel="stylesheet" href="https://fonts.googleapis.com/css2?family=Arimo:wght@400;700&display=swap">
<style>
  :root {
    --page-bg: #e6e6e8;
    --card-white: #ffffff;
    --card-dark: #221c25;
    --brand-blue: #3a63ad;
    --ink: #1b1b1b;
    --ink-soft: #4a4a4a;
  }
  * { margin: 0; padding: 0; box-sizing: border-box; }
  html, body { width: 1200px; height: 900px; overflow: hidden; }
  body {
    background: var(--page-bg);
    font-family: "Arimo", Arial, sans-serif;
    display: flex;
    flex-direction: column;
    align-items: center;
    justify-content: center;
    gap: 40px;
  }
  .card {
    position: relative;
    width: 700px;
    height: 400px;
    box-shadow: 0 6px 18px rgba(0,0,0,0.18);
  }
  /* Front */
  .card-front { background: var(--card-white); }
  .accent-band {
    position: absolute; left: 0; top: 0; bottom: 0;
    width: 22px; background: var(--brand-blue);
  }
  .person { position: absolute; left: 58px; top: 96px; }
  .person-name { color: var(--brand-blue); font-size: 21px; font-weight: 400; }
  .person-title { color: var(--ink-soft); font-size: 14px; margin-top: 10px; }
  .brand {
    position: absolute; right: 40px; top: 38px;
    display: flex; flex-direction: column; align-items: center; gap: 10px;
  }
  .brand-circle { width: 52px; height: 52px; border-radius: 50%; background: var(--brand-blue); }
  .brand-name { color: var(--ink); font-size: 15px; font-weight: 700; letter-spacing: 0.5px; text-transform: uppercase; }
  .address {
    position: absolute; right: 48px; top: 150px;
    text-align: right; color: var(--ink-soft); font-size: 15px; line-height: 1.5;
  }
  .contacts {
    position: absolute; left: 66px; bottom: 48px;
    list-style: none; display: flex; flex-direction: column; gap: 8px;
  }
  .contact-item { display: flex; align-items: center; gap: 8px; color: var(--ink-soft); font-size: 17px; }
  .contact-icon { width: 18px; height: 18px; flex: none; }
  /* Back */
  .card-back {
    background: var(--card-dark);
    display: flex; flex-direction: column; align-items: center; justify-content: center; gap: 26px;
  }
  .back-circle { width: 118px; height: 118px; border-radius: 50%; background: var(--brand-blue); }
  .back-web { color: var(--brand-blue); font-size: 15px; }
</style>
</head>
<body>
  <section class="card card-front">
    <div class="accent-band"></div>
    <div class="person">
      <p class="person-name">Desmond Munkalt</p>
      <p class="person-title">CEO</p>
    </div>
    <div class="brand">
      <div class="brand-circle"></div>
      <p class="brand-name">Tallowreed Advisory Partners</p>
    </div>
    <address class="address" style="font-style:normal">
      718 Quillmore Ave<br>Miami<br>Florida 33190
    </address>
    <ul class="contacts">
      <li class="contact-item">
        <svg class="contact-icon" viewBox="0 0 20 20" aria-hidden="true">
          <circle cx="10" cy="10" r="10" fill="var(--brand-blue)"/>
          <path d="M7 5c.6 0 1.7 2 1.6 2.5-.1.6-1 1-.8 1.6.4 1.2 1.4 2.3 2.6 2.8.6.2 1-.7 1.6-.8.5-.1 2.5 1 2.5 1.6 0 .9-1.2 1.8-2 1.8C9.2 14.5 5.4 10.8 5.2 7c0-.9 1-2 1.8-2z" fill="#fff"/>
        </svg>
        3055 550 148
      </li>
      <li class="contact-item">
        <svg class="contact-icon" viewBox="0 0 20 20" aria-hidden="true">
          <rect width="20" height="20" rx="4" fill="var(--brand-blue)"/>
          <rect x="6.5" y="3.5" width="7" height="13" rx="1.2" fill="none" stroke="#fff" stroke-width="1.4"/>
          <circle cx="10" cy="14" r="0.9" fill="#fff"/>
        </svg>
        9175 550 193
      </li>
      <li class="contact-item">
        <svg class="contact-icon" viewBox="0 0 20 20" aria-hidden="true">
          <circle cx="10" cy="10" r="10" fill="var(--brand-blue)"/>
          <rect x="4.5" y="6.5" width="11" height="7.5" fill="#fff"/>
          <path d="M4.5 6.5l5.5 4.2 5.5-4.2" fill="none" stroke="var(--brand-blue)" stroke-width="1"/>
        </svg>
        dmunkalt@tallowreedadvisory.example
      </li>
    </ul>
  </section>

  <section class="card card-back">
    <div class="back-circle"></div>
    <p class="back-web">www.tallowreedadvisory.example</p>
  </section>
</body>
</html>
```